Poster for homelessness project (2 day deadline)

Amber Lantern Scheme is an initiative in the UK which aims to ensure that people who are new to sleeping on the street are quickly given assistance to take them out of situation they find themselves in.

It began as a London-based project but is now being rolled out nationwide. I am working for a project based in the north of England.

We need some posters which show an image of a place where a rough sleeper may spend the night with some supporting graphic design.

I have three initial images, but I need to be able to easily swap out the images for others. I would appreciate if you could produce three posters for me, each with a different image.

-
Please note:
My client is quite vague about what they want at the moment and the above words may change. I need the selected product to be a layered raw file that I can amend myself with any Adobe CS5.5 (or below) application.

Any typefaces that you choose need to be easily purchasable online.

Please view formatinfo.pdf for formatting guidelines.

Target Market(s)

The general public. It will be placed in public places.

Industry/Entity Type

Graphic Design

Requirements
Must have
• Must contain the words:

"Tonight someone will sleep rough for the first time. Help us make sure they find the Amber Lantern."

"Would you sleep here? Sleeping rough is dangerous. Make sure everyone finds the Amber Lantern."

-
Nice to have
• I'd like this to be quite bleak, grimy and "urban" in feel.

You may recolour/tint the images in any way to enhance this feeling.

```html
<!DOCTYPE html>
<html lang="en">
<head>
<meta charset="utf-8">
<title>Amber Lantern Scheme – Would you sleep here?</title>
<link rel="stylesheet" href="https://fonts.googleapis.com/css2?family=Roboto+Slab:wght@300;400;700&display=swap">
<style>
  :root {
    --ink: #000000;
    --paper: #ffffff;
    --brick-blue: #4b5fd6;
    --brick-mid: #2e3a9c;
    --door-navy: #141a4a;
    --shadow-navy: #0a0c24;
    --band: rgba(0, 0, 0, 0.62);
  }
  * { margin: 0; padding: 0; box-sizing: border-box; }
  html, body {
    width: 800px;
    height: 1200px;
    overflow: hidden;
    background: var(--ink);
  }
  .poster {
    position: relative;
    width: 800px;
    height: 1200px;
    background: var(--ink);
    color: var(--paper);
    font-family: "Roboto Slab", Georgia, serif;
    overflow: hidden;
  }
  .location-photo {
    position: absolute;
    left: 0; top: 0;
    width: 800px;
    height: 980px;
    background:
      linear-gradient(to bottom, rgba(0,0,0,0) 0%, rgba(0,0,0,0) 84%, var(--ink) 100%),
      linear-gradient(to right, var(--brick-blue) 0%, var(--brick-mid) 38%, var(--door-navy) 44%, var(--shadow-navy) 75%, var(--door-navy) 100%);
  }
  .headline-band {
    position: absolute;
    left: 0; top: 175px;
    width: 800px;
    height: 302px;
    background: var(--band);
  }
  .headline {
    position: absolute;
    left: 38px;
    top: 170px;
    font-weight: 700;
    font-size: 92px;
    line-height: 75px;
    letter-spacing: -2px;
  }
  .message {
    position: absolute;
    left: 0; top: 555px;
    width: 800px;
    text-align: center;
    font-weight: 300;
    font-size: 43px;
    line-height: 50px;
  }
  .scheme-mark {
    position: absolute;
    left: 38px;
    top: 896px;
    font-weight: 400;
    font-size: 21px;
    line-height: 22px;
    padding-bottom: 7px;
    border-bottom: 1px solid var(--paper);
    width: 122px;
  }
  .supporting-info {
    position: absolute;
    left: 38px;
    top: 1016px;
    width: 720px;
    font-size: 15px;
    line-height: 20px;
    font-weight: 400;
  }
  .supporting-info h2 {
    font-size: 15px;
    font-weight: 700;
    margin-bottom: 21px;
  }
  .supporting-info p { margin-bottom: 20px; }
</style>
</head>
<body>
  <main class="poster">
    <div class="location-photo" role="img" aria-label="Blue-tinted photograph of a nightclub doorway with brick wall and drainpipe, a place where someone might sleep rough"></div>
    <div class="headline-band"></div>
    <h1 class="headline">Would<br>you<br>sleep<br>here?</h1>
    <p class="message">Sleeping rough is dangerous.<br>Make sure everyone finds<br>the Amber Lantern.</p>
    <div class="scheme-mark">Amber Lantern Scheme</div>
    <section class="supporting-info">
      <h2>Supporting Information:</h2>
      <p>It began as a London-based project but is now being rolled out nationwide. I am working for a project based in the north of England.</p>
      <p>We need some posters which show an image of a place where a rough sleeper may spend the night with some supporting graphic design.</p>
    </section>
  </main>
</body>
</html>
```